Holistic massage therapist

I need a business card for a business made by me, I m an holistic massage therapist, I 'm qualified in reflexology , indian head massage and sweedish body massage, I m working from home or mobile as well, i use massage as a therapy not as a beauty treatment, i m base in London.
I also offer skincare product such as creams or oils and blending with essential oil that I make my self they are completely natural and 100% use of organic product, all the product they are homemade by me.

Industry/Entity Type

Massage

Requirements
Must have
• image that express peace and quite as the massage is an anti stresful remedies for the everyday life

```html
<!DOCTYPE html>
<html lang="en">
<head>
<meta charset="utf-8">
<title>Clara Whitmore – Holistic Massage Therapist</title>
<link rel="stylesheet" href="https://fonts.googleapis.com/css2?family=Lato:wght@400;700&display=swap">
<style>
  :root {
    --backdrop: #e9e4dc;
    --card: #ffffff;
    --accent: #e6587a;
    --art-cream: #f7f1e3;
    --art-pink: #e9c3c8;
    --art-blue: #b9c3da;
  }
  html, body {
    margin: 0;
    width: 1200px;
    height: 1023px;
    overflow: hidden;
    background: var(--backdrop);
  }
  .canvas {
    position: relative;
    width: 1200px;
    height: 1023px;
  }
  .business-card {
    position: absolute;
    left: 350px;
    top: 72px;
    width: 500px;
    height: 860px;
    background: var(--card);
    box-shadow: 0 10px 30px rgba(0,0,0,0.18);
    font-family: "Lato", sans-serif;
    color: var(--accent);
    box-sizing: border-box;
  }
  .card-art {
    position: absolute;
    left: 32px;
    top: 40px;
    width: 436px;
    height: 290px;
    background: linear-gradient(135deg, var(--art-cream) 0%, var(--art-pink) 45%, var(--art-blue) 70%, var(--art-cream) 100%);
  }
  .identity {
    position: absolute;
    left: 52px;
    top: 360px;
    right: 30px;
  }
  .therapist-name {
    margin: 0;
    font-size: 48px;
    font-weight: 400;
    line-height: 1.05;
  }
  .therapist-title {
    margin: 4px 0 0 4px;
    font-size: 24px;
    font-weight: 400;
  }
  .contact-list {
    position: absolute;
    left: 52px;
    right: 20px;
    top: 500px;
    margin: 0;
    padding: 0;
    list-style: none;
    font-size: 25px;
    line-height: 1.5;
    white-space: nowrap;
  }
  .services {
    position: absolute;
    left: 20px;
    right: 20px;
    top: 700px;
    margin: 0;
    text-align: center;
    font-size: 25px;
    line-height: 1.35;
  }
  .edge-band {
    position: absolute;
    left: 0;
    right: 0;
    bottom: 0;
    height: 14px;
    background: var(--accent);
  }
</style>
</head>
<body>
<main class="canvas">
  <article class="business-card">
    <div class="card-art" role="img" aria-label="Soft watercolour illustration of a woman resting on a massage table beside a vase of flowers and a candle"></div>
    <header class="identity">
      <h1 class="therapist-name">Clara Whitmore</h1>
      <p class="therapist-title">Holistic Massage Therapist</p>
    </header>
    <ul class="contact-list">
      <li>T: 020 7946 0321</li>
      <li>M: 07700 900 456</li>
      <li>E: clarawhitmore@example.com</li>
      <li>W: www.clarawhitmore.com</li>
    </ul>
    <p class="services">Reflexology , Indian Head Massage and<br>Swedish Body Massage</p>
    <div class="edge-band"></div>
  </article>
</main>
</body>
</html>
```